Website - Tides Of Bloom

We are catalysts of change in people's lives.
We work with individuals and professionals to bring about instant substantial & transforming change in their lives.
We provide one-on-one lifestyle coaching by an experienced practitioner.
Our existing website is www.tidesofbloom.biz & this site contains our the basis for the content of our desired new project, so please examine this carefully.
We require a professional and captivating website that will instantly impress, engage invite our readers to click & invest their lives.
Our services do not come cheap, but are second to none.
Our website must be contemporary whilst reflecting indisputable class & ultra-confidence in the success of our work.
Target Market(s)
Those who seek to want to change in their lives. Those aged primarily between 30 and 50 years of age, male or female.
Industry/Entity Type
Work
Look and feel

```html
<!DOCTYPE html>
<html lang="en">
<head>
<meta charset="utf-8">
<title>Tides Of Bloom</title>
<link href="https://fonts.googleapis.com/css2?family=Roboto+Condensed:wght@300;400;700&display=swap" rel="stylesheet">
<style>
:root{
  --black:#050505;
  --header:#0b0b0b;
  --tab:#141414;
  --band:#3b3b3b;
  --band-dark:#1c1c1c;
  --ink:#0a0a0a;
  --muted:#8a8a8a;
  --soft:#b9b9b9;
  --pale:#efefef;
  --card:#e6e6e6;
  --white:#ffffff;
}
*{margin:0;padding:0;box-sizing:border-box}
html,body{width:1200px;height:1200px;overflow:hidden;background:var(--white)}
body{position:relative;font-family:"Roboto Condensed",Arial,sans-serif}
.abs{position:absolute}

/* header */
.site-header{left:0;top:0;width:1200px;height:137px;background:linear-gradient(#000,var(--header))}
.brand-mark{left:200px;top:38px;width:62px;height:62px;border-radius:50%;background:#2c2c2c}
.brand-divider{left:291px;top:10px;width:1px;height:117px;background:#555}
.brand-name{left:305px;top:16px;color:#c9c9c9;font-size:41px;font-weight:400;line-height:38px}
.utility{right:180px;top:9px;display:flex;align-items:center;gap:8px;color:#ddd;font-size:10.5px}
.utility .dot{width:8px;height:8px;border-radius:50%;background:#ddd;display:inline-block}
.utility .sep{width:1px;height:13px;background:#666;margin:0 5px}
.main-nav{left:577px;top:86px;display:flex;gap:6px}
.main-nav a{display:block;height:51px;line-height:51px;text-align:center;color:#bdbdbd;font-size:12.5px;text-decoration:none;background:var(--tab);letter-spacing:.5px}
.main-nav a.active{background:#000;color:#fff;font-weight:700}

/* hero */
.hero{left:0;top:137px;width:1200px;height:267px;background:radial-gradient(ellipse 260px 120px at 630px 40px,#e9b45a,#9a6a2c 45%,#3e2c18 80%,#1f1a14)}

/* claims band */
.claims{left:0;top:404px;width:1200px;height:163px;background:var(--band)}
.claims-title{left:200px;top:16px;font-size:61px;line-height:56px;font-weight:300;color:#c8c8c8}
.claims-title b{color:var(--ink);font-weight:700}
.claims-divider{left:472px;top:26px;width:1px;height:116px;background:#777}
.claims-list{left:510px;top:26px;list-style:none}
.claims-list li{display:flex;align-items:center;height:41px;font-size:17.5px;font-weight:700;color:var(--ink)}
.claims-list svg{margin-right:12px}

/* promise band */
.promise{left:0;top:567px;width:1200px;height:147px;background:var(--band-dark);color:var(--soft);font-size:29px;font-weight:300;line-height:39px;text-align:center}
.promise p{position:absolute;top:36px}

/* features */
.feature{top:745px;width:255px;color:var(--muted);font-size:13.5px;line-height:19.3px;font-weight:300}
.feature h2{float:left;margin-right:14px;font-weight:700;color:#999;font-size:58px;line-height:52px}
.feature h2 span{display:block;color:#555;font-size:38px;line-height:44px}
.col-rule{top:748px;width:1px;height:122px;background:#e4e4e4}
.section-rule{left:180px;top:912px;width:844px;height:1px;background:#e2e2e2}

/* testimonials */
.testimonials-title{left:0;width:1200px;top:928px;text-align:center;font-size:38px;font-weight:700;color:#aaa}
.testimonials{left:0;top:977px;width:1200px;height:185px;background:var(--pale)}
.quote{top:15px;width:313px;height:115px;background:var(--card);border-radius:6px;padding:22px 25px;color:#777;font-size:13.5px;line-height:16.5px;font-weight:300}
.quote-author{top:145px;font-size:14px;font-weight:700;color:#666}

/* footer */
.site-footer{left:0;top:1162px;width:1200px;height:38px;background:var(--black);color:#fff;font-size:9.5px;font-weight:700;text-align:center;line-height:38px;letter-spacing:.3px}
</style>
</head>
<body>

<header class="site-header abs">
  <div class="brand-mark abs"></div>
  <div class="brand-divider abs"></div>
  <div class="brand-name abs">Tides Of<br>Bloom</div>
  <div class="utility abs">
    <i class="dot"></i><i class="dot"></i><i class="dot"></i><i class="dot"></i>
    <span class="sep"></span><span>Help</span><span class="sep"></span><span>Cookies Policy</span>
  </div>
  <nav class="main-nav abs">
    <a class="active" href="#" style="width:91px">HOME</a>
    <a href="#" style="width:119px">BUSINESS</a>
    <a href="#" style="width:121px">INDIVIDUAL</a>
    <a href="#" style="width:90px">CONTACT</a>
  </nav>
</header>

<div class="hero abs" role="img" aria-label="Photo of a figure standing on a lakeside path at misty sunrise, framed by silhouetted trees"></div>

<section class="claims abs">
  <h1 class="claims-title abs"><b>Change</b> Is<br>Yours</h1>
  <div class="claims-divider abs"></div>
  <ul class="claims-list abs">
    <li><svg width="32" height="32" viewBox="0 0 32 32"><circle cx="16" cy="16" r="14" fill="none" stroke="#888" stroke-width="2"/><circle cx="16" cy="16" r="8" fill="#777"/><path d="M16 2v28M2 16h28" stroke="#ccc" stroke-width="2"/></svg>Improve your relationships and the ways you communicate</li>
    <li><svg width="32" height="32" viewBox="0 0 32 32"><circle cx="16" cy="16" r="14" fill="none" stroke="#888" stroke-width="2"/><circle cx="16" cy="16" r="8" fill="#777"/><path d="M16 2v28M2 16h28" stroke="#ccc" stroke-width="2"/></svg>More choices about your behaviours and emotions</li>
    <li><svg width="32" height="32" viewBox="0 0 32 32"><circle cx="16" cy="16" r="14" fill="none" stroke="#888" stroke-width="2"/><circle cx="16" cy="16" r="8" fill="#777"/><path d="M16 2v28M2 16h28" stroke="#ccc" stroke-width="2"/></svg>Create better results through becoming a greater thinker</li>
  </ul>
</section>

<section class="promise abs">
  <p style="left:200px;width:346px">Not a lifelong project or years of therapy</p>
  <p style="left:660px;width:350px">Change begins today with our Master Practitioner</p>
</section>

<article class="feature abs" style="left:186px">
  <h2>Our<span>Clients</span></h2>
  Our clients experience their desired instant &amp; permanent transformation, emerging from our consultations ready to take on their world from a vastly different paradigm.
</article>
<div class="col-rule abs" style="left:453px"></div>
<article class="feature abs" style="left:474px;top:741px;width:258px">
  <h2>Our<span>Practitioner</span></h2>
  At Tides Of Bloom, our Master Practitioner will inspire you, shifting your perspective &amp; facilitating your mind with the freedom to realise your dreams.
</article>
<div class="col-rule abs" style="left:748px"></div>
<article class="feature abs" style="left:773px;top:736px;width:240px">
  <h2>Join<span>Us</span></h2>
  Join Dana Whitford, Marcus Hale, R.T. Lowell, Owen Stacey, Leon Marsh, Nina Calloway and hundreds of thousands of others who are achieving the life changing, consistent results you are dreaming of now.
</article>
<div class="section-rule abs"></div>

<h2 class="testimonials-title abs">Testimonials</h2>
<section class="testimonials abs">
  <blockquote class="quote abs" style="left:181px">“Lorem ipsum dolor sit amet, consectetuer adipiscing elit, sed diam nonummy nibh euismod tincidunt ut laoreet dolore magna aliquam erat volutpat. ”</blockquote>
  <div class="quote-author abs" style="left:252px">MR. JHON DOE</div>
  <blockquote class="quote abs" style="left:505px">“Duis autem vel eum iriure dolor in hendrerit in vulputate velit esse molestie consequat, vel illum dolore eu feugiat nulla facilisis at vero eros et accumsan et iusto odio.”</blockquote>
  <div class="quote-author abs" style="left:575px">MR. JHON DOE</div>
</section>

<footer class="site-footer abs">Copyright 2013 Tides Of Bloom. All Rights Reserved</footer>

</body>
</html>
```